A new company focused on starting and investing in transformative businesses.

We need a simple and clean website with a few pages. we like larkmeadow.com as a starting point. we want the landing page to be very simple with an option to click through on the top right into INVESTOR LOGIN. then we want to be able to scroll down to see more about our company.

Target Market(s)

professional

Coding

Coded - Design and coding required

Number of Pages Required

2 page

Font styles to use
Serif
Sans Serif

Requirements
Must have
• HALVERN BUILDERS logo (attached as a file) on the top with INVESTOR LOGIN as a click through on the right. Please model the click through from larkmeadow.com. The description (also written in attached file) should be on the landing page. we do not want to have to scroll to read the description.

Then we can scroll down to read more about Halvern including the mission and the two types of businesses. More is detailed on the attached file called "Halvern Website Syntax"
Should not have
• should not be slow loading with lots of fancy graphics. should not be busy and with too many colors.

```html
<!DOCTYPE html>
<html lang="en">
<head>
<meta charset="utf-8">
<title>Halvern Builders</title>
<link href="https://fonts.googleapis.com/css2?family=Tinos&family=Noto+Serif:wght@700&family=Poppins:wght@300;400;600&family=Barlow+Semi+Condensed:wght@500&display=swap" rel="stylesheet">
<style>
  :root {
    --brand-blue: #0d67a0;
    --pale-blue: #cde0ec;
    --ink: #111111;
    --body-grey: #5f6368;
    --footer-grey: #a9a9a9;
    --white: #ffffff;
    --black: #000000;
  }
  * { margin: 0; padding: 0; box-sizing: border-box; }
  html, body { width: 802px; height: 1200px; overflow: hidden; background: var(--white); }
  .page { position: relative; width: 802px; height: 1200px; font-family: "Poppins", sans-serif; color: var(--ink); }
  .abs { position: absolute; }

  /* Hero */
  .hero { left: 0; top: 0; width: 802px; height: 451px;
    background: linear-gradient(100deg, #4a5a52 0%, #5c6468 30%, #4e5a6c 55%, #6b6f74 80%, #55595e 100%); }
  .hero::after { content: ""; position: absolute; inset: 0; background: rgba(20,24,30,0.35); }
  .brand { font-family: "Poppins", sans-serif; font-weight: 600; letter-spacing: 0.5px; line-height: 1.05; }
  .brand-mark { display: inline-block; width: 10px; height: 10px; margin-right: 7px; vertical-align: top; margin-top: 3px; }
  .hero-brand { left: 40px; top: 14px; z-index: 2; color: var(--white); font-size: 14px; }
  .hero-brand .brand-mark { background: var(--white); }
  .investor-login { left: 657px; top: 10px; width: 104px; height: 27px; border-radius: 14px; background: var(--brand-blue);
    z-index: 2; display: flex; align-items: center; font-family: "Barlow Semi Condensed", sans-serif; font-weight: 500;
    font-size: 10.5px; color: var(--white); text-decoration: none; padding-left: 16px; }
  .investor-login .login-pill { background: var(--black); border-radius: 12px; padding: 4px 8px 4px 4px; margin-left: 1px; }
  .hero-title { left: 150px; top: 188px; width: 502px; z-index: 2; text-align: center; color: var(--white);
    font-family: "Tinos", serif; font-size: 27px; line-height: 30.5px; }

  /* Welcome */
  .welcome-art { left: 0; top: 451px; width: 802px; height: 330px; }
  .welcome-brand { left: 105px; top: 505px; color: #1f2a36; font-size: 13px; }
  .welcome-brand .brand-mark { background: var(--brand-blue); }
  .welcome-rule { left: 105px; top: 541px; width: 25px; height: 1px; background: var(--ink); }
  .welcome-title { left: 106px; top: 549px; font-family: "Noto Serif", serif; font-weight: 700; font-size: 20px; letter-spacing: 0.5px; }
  .mission { left: 106px; top: 584px; width: 240px; font-size: 9.6px; line-height: 15px; color: var(--body-grey); font-weight: 300; }
  .mission strong { color: var(--brand-blue); font-weight: 600; }

  /* Types of businesses */
  .team-photo-backing { left: 61px; top: 855px; width: 108px; height: 109px; background: #d6e5f0; }
  .team-photo { left: 85px; top: 739px; width: 226px; height: 201px;
    background: linear-gradient(135deg, #d8d6d2 0%, #b9b4ae 40%, #6f7a86 70%, #3b4452 100%); }
  .types-title { left: 347px; top: 740px; font-family: "Noto Serif", serif; font-weight: 700; font-size: 21px; }
  .icon-box { width: 40px; height: 40px; background: var(--white); box-shadow: 0 1px 5px rgba(0,0,0,0.1);
    display: flex; align-items: center; justify-content: center; }
  .icon-ground { left: 346px; top: 784px; }
  .icon-special { left: 349px; top: 889px; }
  .biz-title { font-size: 13px; font-weight: 400; color: var(--ink); }
  .biz-body { font-size: 8.4px; line-height: 13px; color: var(--body-grey); font-weight: 300; margin-top: 2px; }
  .biz-ground { left: 408px; top: 782px; width: 232px; }
  .biz-special { left: 409px; top: 887px; width: 232px; }

  /* Footer */
  .site-footer { left: 0; top: 1015px; width: 802px; height: 160px; background: var(--black); color: var(--white); text-align: center; }
  .footer-brand { display: inline-block; margin-top: 38px; font-size: 15px; color: var(--white); text-align: left; }
  .footer-brand .brand-mark { background: var(--white); }
  .footer-text { width: 330px; margin: 14px auto 0; font-size: 8.4px; line-height: 13px; color: var(--footer-grey); }
  .footer-email { margin-top: 8px; font-size: 8.6px; display: flex; align-items: center; justify-content: center; gap: 6px; }
  .legal-bar { left: 0; top: 1175px; width: 802px; height: 25px; background: var(--brand-blue); color: var(--white);
    font-size: 8.4px; text-align: center; line-height: 25px; }
</style>
</head>
<body>
<div class="page">

  <header class="hero abs" role="img" aria-label="Photo of a man with glasses reading a tablet in a bright living room"></header>
  <div class="hero-brand brand abs"><span class="brand-mark"></span>HALVERN<br><span style="padding-left:17px">BUILDERS</span></div>
  <a class="investor-login abs" href="#">INVESTOR<span class="login-pill">LOGIN</span></a>
  <h1 class="hero-title abs">Halvern Builders is an entrepreneurial firm focused on building and growing transformational companies</h1>

  <svg class="welcome-art abs" viewBox="0 451 802 330" width="802" height="330">
    <defs>
      <linearGradient id="officePhoto" x1="0" y1="0" x2="1" y2="1">
        <stop offset="0" stop-color="#c4c6c8"/>
        <stop offset="0.5" stop-color="#b2b0ad"/>
        <stop offset="1" stop-color="#8f96a0"/>
      </linearGradient>
    </defs>
    <polygon points="0,451 299,451 0,676" fill="var(--pale-blue)"/>
    <polygon points="351,451 802,451 802,777" fill="url(#officePhoto)" role="img" aria-label="Photo of two smiling women reviewing papers in an office"/>
    <line x1="239" y1="451" x2="515" y2="626" stroke="var(--brand-blue)" stroke-width="1"/>
  </svg>

  <div class="welcome-brand brand abs"><span class="brand-mark"></span>HALVERN<br><span style="padding-left:17px">BUILDERS</span></div>
  <div class="welcome-rule abs"></div>
  <h2 class="welcome-title abs">WELCOME</h2>
  <p class="mission abs">Our mission is to build <strong>meaningful</strong> businesses that create <strong>enduring</strong> value by impacting people in a <strong>measurable</strong> way.</p>

  <div class="team-photo-backing abs"></div>
  <div class="team-photo abs" role="img" aria-label="Photo of two colleagues smiling at a computer screen"></div>

  <h2 class="types-title abs">Types of businesses</h2>

  <div class="icon-box icon-ground abs">
    <svg width="28" height="26" viewBox="0 0 28 26" fill="none" stroke="var(--brand-blue)" stroke-width="1.1">
      <circle cx="8" cy="6" r="3.5"/><circle cx="20" cy="6" r="3.5"/><circle cx="14" cy="14" r="3.5"/>
      <path d="M2 17c0-4 3-6 6-6M26 17c0-4-3-6-6-6M7 25c0-4 3-7 7-7s7 3 7 7z"/>
    </svg>
  </div>
  <div class="biz-ground abs">
    <h3 class="biz-title">Ground Up</h3>
    <p class="biz-body">Our ground up business applies a proven analytic process to identify value edge, a form of competitive advantage. We architect transformational companies and are deliberate in creating the foundation necessary to lead an industry.</p>
  </div>

  <div class="icon-box icon-special abs">
    <svg width="30" height="30" viewBox="0 0 30 30" fill="none" stroke="var(--brand-blue)" stroke-width="1.1">
      <circle cx="18" cy="18" r="10"/><circle cx="11" cy="10" r="6.5"/><path d="M6.5 14.5L2 19"/>
      <circle cx="11" cy="9" r="2"/><path d="M7.5 14c1-2 6-2 7 0"/>
      <circle cx="21" cy="19" r="2"/><path d="M18 24c1-2 5-2 6 0"/>
    </svg>
  </div>
  <div class="biz-special abs">
    <h3 class="biz-title">Special Opportunities</h3>
    <p class="biz-body">We partner with exceptional teams that create value by transforming lives. Our investment focus includes large companies and spin-outs.</p>
  </div>

  <footer class="site-footer abs">
    <div class="footer-brand brand"><span class="brand-mark"></span>HALVERN<br><span style="padding-left:17px">BUILDERS</span></div>
    <p class="footer-text">Halvern Builders is an entrepreneurial firm focused on building and growing transformational companies</p>
    <p class="footer-email">
      <svg width="19" height="12" viewBox="0 0 19 12"><rect width="19" height="12" fill="var(--white)"/><path d="M0 0l9.5 6.5L19 0" fill="none" stroke="var(--black)" stroke-width="1.4"/></svg>
      mara@halvernbuilders.com
    </p>
  </footer>
  <div class="legal-bar abs">©2021 halvernbuilders-All Right Reserved.</div>

</div>
</body>
</html>
```